Dental office stationary (letterhead, envelopes), business cards, presentation folders

Nothing too dental outside of the logo. I will need all stationary, presentation folders, business cards. Would prefer to stay in the colors of the logo

Gordon Plaskett, DDS
Brightvale Dental Implant Center
772-555-0187
info@brightvaledental-example.com
3875 NW Orchard Pkwy Unit B
Stuart, FL 34917

Also need appointment date and time
And cancellation policy
I want it to say “kindly ask for
A 48hr cancellation policy to avoid incurring a cancellation fee”

Dental

Colors
0054AA
0677BA
7BADD7
CADEEF
E8F1F8

Requirements
Must have
• Name of your office, name of doctor, address, phone number
Should not have
• Too much tooth/dental. Only the tooth in logo

```html
<!DOCTYPE html>
<html lang="en">
<head>
<meta charset="utf-8">
<title>Brightvale Dental Implant Center – Business Card</title>
<link href="https://fonts.googleapis.com/css2?family=Cinzel:wght@500;600&family=Open+Sans:wght@400;600&display=swap" rel="stylesheet">
<style>
  :root {
    --navy: #0054AA;
    --blue: #0677BA;
    --sky: #7BADD7;
    --mist: #CADEEF;
    --ice: #E8F1F8;
    --teal: #1FB5A6;
    --ink: #4a4a4a;
    --rule: #c9c9c9;
    --stage: #eef1f4;
    --paper: #ffffff;
  }
  * { box-sizing: border-box; margin: 0; padding: 0; }
  html, body { width: 1200px; height: 874px; overflow: hidden; }
  body {
    background: var(--stage);
    display: flex;
    flex-direction: column;
    align-items: center;
    justify-content: center;
    gap: 48px;
    font-family: "Open Sans", Arial, sans-serif;
  }
  .card {
    position: relative;
    width: 620px;
    height: 354px;
    border-radius: 22px;
    overflow: hidden;
    box-shadow: 0 6px 18px rgba(0, 40, 90, 0.18);
  }

  /* Front */
  .card-front {
    background: radial-gradient(ellipse at 50% 45%, #1d95d8 0%, #0a7cc4 55%, var(--blue) 100%);
    display: flex;
    align-items: center;
    justify-content: center;
  }
  .brand-name {
    font-family: "Cinzel", Georgia, serif;
    font-weight: 600;
    text-align: center;
    line-height: 1.1;
  }
  .card-front .brand-name { color: var(--navy); }
  .brand-name .brand-main { display: block; font-size: 48px; letter-spacing: 1px; }
  .brand-name .brand-sub { display: block; font-size: 14px; letter-spacing: 5px; margin-top: 6px; }

  /* Back */
  .card-back { background: var(--paper); }
  .card-back .brand-name {
    position: absolute;
    top: 60px;
    right: 40px;
    color: var(--blue);
  }
  .card-back .brand-name .brand-main { font-size: 36px; }
  .card-back .brand-name .brand-sub { font-size: 10.5px; letter-spacing: 3.6px; }

  .doctor {
    position: absolute;
    left: 44px;
    top: 146px;
  }
  .doctor-name {
    font-family: "Cinzel", Georgia, serif;
    font-weight: 600;
    font-size: 25px;
    color: var(--blue);
    letter-spacing: 0.5px;
    line-height: 1.2;
  }
  .doctor-title {
    font-size: 13px;
    color: var(--teal);
    line-height: 1.3;
  }
  .contact-list {
    position: absolute;
    left: 44px;
    top: 200px;
    list-style: none;
    font-size: 14px;
    color: var(--ink);
  }
  .contact-list li {
    display: flex;
    align-items: center;
    gap: 10px;
    height: 21px;
  }
  .contact-list svg { width: 13px; height: 13px; fill: var(--blue); flex: none; }

  .divider {
    position: absolute;
    left: 36px;
    right: 70px;
    top: 268px;
    height: 1px;
    background: var(--rule);
  }
  .address {
    position: absolute;
    right: 76px;
    top: 274px;
    text-align: right;
    font-size: 14px;
    line-height: 19px;
    color: var(--ink);
    font-style: normal;
  }
  .card-band {
    position: absolute;
    left: 0; right: 0; bottom: 0;
    height: 18px;
    background: linear-gradient(90deg, var(--blue), #1a93d4);
    border-top: 3px solid var(--teal);
    box-shadow: 0 -4px 0 var(--paper), 0 -5px 0 var(--mist);
  }
</style>
</head>
<body>

  <section class="card card-front" aria-label="Business card front">
    <div class="brand-name">
      <span class="brand-main">BRIGHTVALE</span>
      <span class="brand-sub">DENTAL IMPLANT CENTER</span>
    </div>
  </section>

  <section class="card card-back" aria-label="Business card back">
    <div class="brand-name">
      <span class="brand-main">BRIGHTVALE</span>
      <span class="brand-sub">DENTAL IMPLANT CENTER</span>
    </div>

    <div class="doctor">
      <p class="doctor-name">GORDON PLASKETT</p>
      <p class="doctor-title">DDS</p>
    </div>

    <ul class="contact-list">
      <li>
        <svg viewBox="0 0 24 24" aria-hidden="true"><path d="M6.6 10.8a15.1 15.1 0 0 0 6.6 6.6l2.2-2.2c.3-.3.7-.4 1-.2 1.1.4 2.3.6 3.6.6.6 0 1 .4 1 1V20c0 .6-.4 1-1 1A17 17 0 0 1 3 4c0-.6.4-1 1-1h3.5c.6 0 1 .4 1 1 0 1.3.2 2.5.6 3.6.1.3 0 .7-.2 1z"/></svg>
        <span>772-555-0187</span>
      </li>
      <li>
        <svg viewBox="0 0 24 24" aria-hidden="true"><path d="M2 5h20v14H2zm2 2v.5l8 5 8-5V7l-8 5z"/></svg>
        <span>info@brightvaledental-example.com</span>
      </li>
      <li>
        <svg viewBox="0 0 24 24" aria-hidden="true"><path d="M12 2a10 10 0 1 0 0 20 10 10 0 0 0 0-20zm6.9 6h-2.9a15 15 0 0 0-1.4-3.6A8 8 0 0 1 18.9 8zM12 4c.8 1.2 1.5 2.5 1.9 4h-3.8c.4-1.5 1.1-2.8 1.9-4zM4.3 14a8 8 0 0 1 0-4h3.4a16 16 0 0 0 0 4zm.8 2h2.9c.3 1.3.8 2.5 1.4 3.6A8 8 0 0 1 5.1 16zM8 8H5.1a8 8 0 0 1 4.3-3.6C8.8 5.5 8.3 6.7 8 8zm4 12c-.8-1.2-1.5-2.5-1.9-4h3.8c-.4 1.5-1.1 2.8-1.9 4zm2.3-6H9.7a14.6 14.6 0 0 1 0-4h4.6a14.6 14.6 0 0 1 0 4zm.3 5.6c.6-1.1 1.1-2.3 1.4-3.6h2.9a8 8 0 0 1-4.3 3.6zm1.7-5.6a16 16 0 0 0 0-4h3.4a8 8 0 0 1 0 4z"/></svg>
        <span>www.brightvaledental-example.com</span>
      </li>
    </ul>

    <div class="divider"></div>

    <address class="address">
      3875 NW Orchard Pkwy Unit B<br>
      Stuart, FL 34917
    </address>

    <div class="card-band"></div>
  </section>

</body>
</html>
```